PowerPoint Presentation

We are looking for a new PPT layout template existing of a cover page, three internal pages - one with text bullets, one with a picture/information and one with more of a table for pricing information and the last a last "thank you - contact info" page. Feel free to grab any graphics from our website at www.brightharbor.com

Any product can be chosen from our products page. Colors are cyan and orange and feel free to choose darker backgrounds for the front and end page. Also included in the graphics is our new business card design.

Also note we are updating our website, and have attached a sample of how it looks for reference.

Reason: We are still looking for submissions for our PowerPoint presentation. We have increased the award amount as well.

Target Market(s)

Target market is private industry professionals, public safety organizations, and state and local government agencies.

Industry/Entity Type

Business

Colors
33a6d7
86cae6
cee9f5
f68d4d
f8ba93
fce2d4

```html
<!DOCTYPE html>
<html lang="en">
<head>
<meta charset="utf-8">
<title>Oil &amp; Gas Communications Solutions</title>
<link rel="stylesheet" href="https://fonts.googleapis.com/css2?family=Open+Sans:wght@300;400;600&display=swap">
<style>
  :root {
    --cyan: #33a6d7;
    --cyan-light: #86cae6;
    --cyan-pale: #cee9f5;
    --orange: #f68d4d;
    --text-grey: #5f6062;
    --logo-grey: #6d6e71;
    --dots: #b9b9b9;
    --frame: #cfcfcf;
    --paper: #ffffff;
  }
  html, body {
    margin: 0;
    padding: 0;
    overflow: hidden;
    background: var(--paper);
  }
  .slide {
    position: relative;
    width: 1200px;
    height: 878px;
    overflow: hidden;
    background: var(--paper);
    font-family: "Open Sans", Arial, sans-serif;
  }
  .slide-title {
    position: absolute;
    left: 72px;
    top: 52px;
    margin: 0;
    font-weight: 300;
    font-size: 54px;
    line-height: 1.1;
    color: var(--cyan);
    letter-spacing: -0.3px;
  }
  .slide-intro {
    position: absolute;
    left: 74px;
    top: 132px;
    width: 1080px;
    margin: 0;
    font-weight: 300;
    font-size: 25.5px;
    line-height: 35px;
    color: var(--cyan-light);
  }
  .price-list {
    position: absolute;
    left: 0;
    top: 0;
    margin: 0;
    padding: 0;
    list-style: none;
  }
  .price-row {
    position: absolute;
    left: 0;
    width: 900px;
    height: 94px;
  }
  .product-thumb {
    position: absolute;
    left: 79px;
    top: 7px;
    width: 107px;
    height: 76px;
    box-sizing: border-box;
    border: 5px solid var(--frame);
  }
  .thumb-dish    { background: linear-gradient(160deg, #f2f4f5, #c9cfd3); }
  .thumb-trailer { background: linear-gradient(180deg, #8fb3cf 0%, #b8a88d 55%, #8d8576 100%); }
  .thumb-case    { background: linear-gradient(180deg, #cfd6dc 0%, #9d9a90 55%, #6b6b66 100%); }
  .thumb-monitor { background: linear-gradient(180deg, #5f93c9 0%, #a9c6e0 50%, #7b8d5e 100%); }
  .thumb-roof    { background: linear-gradient(180deg, #6fa3d6 0%, #dfe6ec 60%, #f2f2f2 100%); }
  .product-name {
    position: absolute;
    left: 224px;
    top: 32px;
    margin: 0;
    font-weight: 400;
    font-size: 19.5px;
    color: var(--text-grey);
    white-space: nowrap;
  }
  .product-name .bullet {
    color: var(--orange);
    font-weight: 600;
    margin-right: 9px;
  }
  .product-price {
    position: absolute;
    right: 74px;
    top: 22px;
    width: 200px;
    text-align: right;
    font-weight: 600;
    font-size: 31px;
    color: var(--cyan-light);
    white-space: nowrap;
  }
  .product-price .cents {
    font-size: 16px;
    vertical-align: 14px;
  }
  .rule {
    position: absolute;
    height: 0;
    border-top: 2px dotted var(--dots);
  }
  .rule-name  { left: 213px; width: 444px; }
  .rule-price { left: 687px; width: 149px; }
  .brand-name {
    position: absolute;
    right: 60px;
    top: 779px;
    margin: 0;
    font-weight: 600;
    font-size: 27px;
    letter-spacing: 0.5px;
    color: var(--logo-grey);
  }
  .footer-band {
    position: absolute;
    left: 0;
    top: 827px;
    width: 1200px;
    height: 51px;
    border-top: 9px solid var(--orange);
    box-sizing: border-box;
    background: repeating-linear-gradient(180deg, var(--cyan) 0 2px, #5cb8e0 2px 4px);
  }
</style>
</head>
<body>
<main class="slide">
  <h1 class="slide-title">Oil &amp; Gas Communications Solutions</h1>
  <p class="slide-intro">Our broad line of fixed, mobile, carry portable and maritime systems satellite solutions are tailored to fit your unique location requirement.</p>

  <div class="rule rule-name" style="top:233px"></div>
  <div class="rule rule-price" style="top:233px"></div>

  <ul class="price-list">
    <li class="price-row" style="top:232px">
      <div class="product-thumb thumb-dish" role="img" aria-label="Photo of a fixed transportable motorized satellite dish"></div>
      <p class="product-name"><span class="bullet">&gt;</span>Fixed Transportable Motorized Satellite Dish</p>
      <span class="product-price">$ 0.000<span class="cents">.00</span></span>
    </li>
    <li class="price-row" style="top:325px">
      <div class="product-thumb thumb-trailer" role="img" aria-label="Photo of a communications trailer with satellite dish"></div>
      <p class="product-name"><span class="bullet">&gt;</span>Communications Trailers</p>
      <span class="product-price">$ 0.000<span class="cents">.00</span></span>
    </li>
    <li class="price-row" style="top:419px">
      <div class="product-thumb thumb-case" role="img" aria-label="Photo of a case based VSAT system set up outdoors"></div>
      <p class="product-name"><span class="bullet">&gt;</span>Case Based VSAT System</p>
      <span class="product-price">$ 0.000<span class="cents">.00</span></span>
    </li>
    <li class="price-row" style="top:512px">
      <div class="product-thumb thumb-monitor" role="img" aria-label="Photo of a remote monitoring station on a pole in open country"></div>
      <p class="product-name"><span class="bullet">&gt;</span>Remote Monitoring &amp; Control</p>
      <span class="product-price">$ 000<span class="cents">.00</span></span>
    </li>
    <li class="price-row" style="top:605px">
      <div class="product-thumb thumb-roof" role="img" aria-label="Photo of a vehicle with a roof mounted VSAT antenna"></div>
      <p class="product-name"><span class="bullet">&gt;</span>Mobile Roof Mounted VSAT Solutions</p>
      <span class="product-price">$ 0.000<span class="cents">.00</span></span>
    </li>
  </ul>

  <div class="rule rule-name" style="top:324px"></div>
  <div class="rule rule-price" style="top:324px"></div>
  <div class="rule rule-name" style="top:418px"></div>
  <div class="rule rule-price" style="top:418px"></div>
  <div class="rule rule-name" style="top:511px"></div>
  <div class="rule rule-price" style="top:511px"></div>
  <div class="rule rule-name" style="top:604px"></div>
  <div class="rule rule-price" style="top:604px"></div>
  <div class="rule rule-name" style="top:697px"></div>
  <div class="rule rule-price" style="top:697px"></div>

  <p class="brand-name">BRIGHTHARBOR</p>

  <div class="footer-band"></div>
</main>
</body>
</html>
```